French flying club (aeroclub) complete wordpress theme

We need a complete wordpress theme to overhaul the look and feel of our aeroclub website.

We are a flying club (aeroclub) based in France, near Paris. We are a non-profit organization providing VFR flight training to members of all ages; our instructors all have extensive experience flying professionally (one of them was captain on the Veltrane!) We have a fleet of 3 aircraft of the same type (Tarsel) that we provide to our members at competitive rates: since we are a non-profit, there are no unnecessary margins on what we charge aside from what’s necessary for renewal of a fun-to-fly fleet!

The club has a very old history (founded in 1950), and was initially founded by female pioneers of aviation in France (corps founded in 1934), serving as flying nurses for the French army in various conflicts and for search-and-rescue missions. Now of course we accept all types of applicants! Our members are genuinely passionate about flying, they care more about time airborne than about the glamour surrounding aviation (not that it does not matter).

We are launching this website design contest because our current website (http://www.aeroclub-velnor.org/) is somewhat stuck in the ‘90s, and we’d like to give it a new look and feel.

Some designs that caught our attention, to draw inspiration from:
- http://www.ventoprelclub.fr/
- http://www.nuagebastide.com/
- http://www.institut-carvalle.com/

Idea would be to provide front page access to the latest pictures and movies taken from our latest flights, a few breaking news, and one click access to a few sections, e.g.:
- our fleet/prices
- instruction options (VFR, night VFR, BIA etc.)
- location and contact info
- history
- a members-private login page for aircraft reservation and planning access, supporting some sort of forum/message board would etc.

When it comes to style, we’re looking for things that relate to our logo colors (blue dominant with some red and white). Our logo can be found at http://www.aeroclub-velnor.org/images/banners_logos/logo_velnor.gif (we can provide a higher resolution one upon request).

Attached are a few excerpts from existing pages (zip file). They're in French but content is usually self-explanatory. Explanations can be provided if necessary.

Target Market(s)

We tend to have various ‘segments’ of users:
- Teenagers and young adults looking to learn flying
- Seniors looking to learn flying
- Experienced pilots who are looking for a no-nonsense, flying enthusiast community

Industry/Entity Type

Club

Font styles to use
Sans Serif

Requirements
Must have
• Theme should be supplied as a self-deployable wordpress package that can be deployed on a fresh instance of wordpress (i.e. wordpress-compatible zip archive)

```html
<!DOCTYPE html>
<html lang="fr">
<head>
<meta charset="utf-8">
<title>Aéro-club Velnor</title>
<link href="https://fonts.googleapis.com/css2?family=Open+Sans:wght@400;600;700&display=swap" rel="stylesheet">
<style>
:root{
  --blue:#1f5fb4;
  --blue-dark:#164a8f;
  --red:#e2202a;
  --text:#4a4f57;
  --muted:#8a9099;
  --sky:#9cb6d6;
  --line:#d6dde6;
  --white:#ffffff;
}
*{box-sizing:border-box;margin:0;padding:0}
html,body{width:1200px;height:2640px;overflow:hidden;background:var(--white)}
body{position:relative;font-family:'Open Sans',sans-serif;color:var(--text);font-size:13px;line-height:1.55}
.site-header{height:88px;display:flex;align-items:center;justify-content:space-between;padding:0 40px;background:var(--white)}
.brand{display:flex;align-items:center;gap:12px}
.brand-mark{width:60px;height:60px;border-radius:50%;background:var(--blue)}
.brand-name{font-weight:700;font-size:18px;color:var(--blue)}
.main-nav{display:flex;height:40px;background:var(--blue)}
.main-nav a{display:flex;align-items:center;padding:0 20px;color:var(--white);font-size:13px;font-weight:600;text-decoration:none}
.main-nav a.is-active{background:var(--red)}
.hero{height:572px;background:linear-gradient(180deg,#6f9bd0 0%,#9dbbdf 45%,#c9d3dc 62%,#7d8590 78%,#5c6269 100%)}
.section{padding:0 80px}
.section-title{font-size:17px;font-weight:700;color:var(--blue);padding-bottom:8px;border-bottom:2px solid var(--blue);display:inline-block;margin-bottom:24px}
.section-title.red{color:var(--red);border-color:var(--red)}
.news{margin-top:80px;display:flex;gap:24px}
.news-text{width:556px}
.news-lead{display:flex;gap:14px;margin-bottom:14px}
.portrait{width:70px;height:86px;flex:none;background:linear-gradient(#c9b8a6,#7c6e62)}
.news-lead h3{font-size:13px;color:var(--blue);font-weight:700;margin-bottom:4px}
.news-text p{margin-bottom:12px}
.red-text{color:var(--red);font-weight:700}
.news-grid{flex:1;display:grid;grid-template-columns:1fr 1fr;grid-template-rows:repeat(3,166px);gap:12px;margin-top:10px}
.photo{background:linear-gradient(160deg,#b7c9dd,#7c8fa6)}
.photo.dark{background:linear-gradient(160deg,#6c737c,#2f343a)}
.photo.green{background:linear-gradient(160deg,#a9c0d8,#7f9a70)}
.infos{margin-top:32px}
.gallery{display:grid;grid-template-columns:repeat(4,1fr);grid-template-rows:200px 200px;gap:12px}
.booking{margin-top:52px}
.booking-body{display:flex;gap:32px}
.booking-photo{width:540px;height:440px;flex:none;background:linear-gradient(180deg,#b9cde3 0%,#d7e0ea 50%,#8e969e 75%,#6f767d 100%)}
.booking-text p{margin-bottom:12px}
.booking-text h4{font-size:13px;color:var(--blue);margin:6px 0 10px}
.booking-text ul{list-style:none}
.booking-text li{position:relative;padding-left:18px;margin-bottom:12px}
.booking-text li::before{content:"";position:absolute;left:0;top:6px;width:8px;height:8px;border-radius:50%;background:var(--blue)}
.site-footer{position:absolute;left:0;top:2408px;width:1200px;height:232px;background:var(--blue);color:var(--white);padding:34px 80px 0}
.footer-row{display:flex;justify-content:space-between}
.footer-title{font-weight:700;font-size:14px;margin-bottom:18px}
.footer-cols{display:flex;gap:60px}
.address{display:flex;gap:10px;width:300px;font-size:12px}
.address svg{flex:none;margin-top:2px}
.follow{text-align:right}
.social{display:flex;gap:10px;justify-content:flex-end}
.social span{width:34px;height:34px;border-radius:50%;background:var(--white)}
.copyright{font-size:11px;margin-top:70px;text-align:right;opacity:.85}
</style>
</head>
<body>
<header class="site-header">
  <div class="brand"><span class="brand-mark"></span><span class="brand-name">Aéro-club Velnor</span></div>
  <nav class="main-nav">
    <a class="is-active" href="#">Vie du club</a><a href="#">Actualité</a><a href="#">Événements</a><a href="#">Infos utiles</a><a href="#">Tradition</a><a href="#">Contacts</a><a href="#">Réservation</a><a href="#">Adhérents</a>
  </nav>
</header>

<div class="hero" role="img" aria-label="Avion léger blanc sur le tarmac sous un ciel bleu"></div>

<section class="section news">
  <div class="news-text">
    <h2 class="section-title">Actualité</h2>
    <div class="news-lead">
      <div class="portrait" role="img" aria-label="Portrait de l'instructeur"></div>
      <div>
        <h3>Julien Marsac : un nouvel instructeur au Velnor</h3>
        <p>Julien Marsac a rejoint l'équipe des instructeurs du club. Pilote de ligne expérimenté, il partagera avec nos élèves sa passion du vol et son goût de la précision.</p>
      </div>
    </div>
    <p><span class="red-text">SORTIES CLUB 2015</span><br>Les sorties club sont ouvertes aux membres brevetés :</p>
    <p>Sam 19 juin / Lun 21 juin : Tours<br>Dimanche 4 juin : Plage de Normandie<br>Dimanche 11 juin : Chambéry Aix-les-Bains<br>Dimanche 2 juillet : Vallée de la Loire<br>Sam 23 / Lun 25 juillet : Corse, sortie en vol de nuit<br>Dimanche 6 septembre : La Rochelle, île de Ré et Oléron<br>Dimanche 20 septembre : Deauville</p>
    <p>Pour chaque date, une affectation sera proposée à chaque pilote volontaire.</p>
    <p>La gestion des sorties club est assurée par le bureau, contactez-le pour vous inscrire.</p>
    <p>Bientôt un atelier instructeur et sécurité. <span class="red-text">Inscriptions ouvertes</span> sur le site du club.</p>
    <p>Et sur les sites officiels si besoin.</p>
  </div>
  <div class="news-grid">
    <div class="photo" role="img" aria-label="Avion du club en vol"></div>
    <div class="photo dark" role="img" aria-label="Tableau de bord d'un avion"></div>
    <div class="photo" role="img" aria-label="Pilote près d'un avion"></div>
    <div class="photo" role="img" aria-label="Avions stationnés sur l'aérodrome"></div>
    <div class="photo green" role="img" aria-label="Avion au sol sur l'herbe"></div>
    <div class="photo" role="img" aria-label="Membres du club devant un avion"></div>
  </div>
</section>

<section class="section infos">
  <h2 class="section-title red">Infos utiles</h2>
  <div class="gallery">
    <div class="photo" role="img" aria-label="Avion de la flotte au sol"></div>
    <div class="photo dark" role="img" aria-label="Instruments de bord"></div>
    <div class="photo" role="img" aria-label="Avion en roulage"></div>
    <div class="photo dark" role="img" aria-label="Vue du cockpit"></div>
    <div class="photo" role="img" aria-label="Avion sur le parking"></div>
    <div class="photo dark" role="img" aria-label="Panneau d'instruments"></div>
    <div class="photo green" role="img" aria-label="Aérodrome et hangar"></div>
    <div class="photo" role="img" aria-label="Avion du club devant le hangar"></div>
  </div>
</section>

<section class="section booking">
  <h2 class="section-title">Planavi - la réservation d'avions par internet</h2>
  <div class="booking-body">
    <div class="booking-photo" role="img" aria-label="Avion blanc stationné avec un pilote à côté"></div>
    <div class="booking-text">
      <p>Depuis le printemps, vous pouvez réserver les avions du club directement en ligne. L'outil est simple, rapide et accessible à tous les membres à jour de cotisation.</p>
      <p>Pour cela, connectez-vous avec votre identifiant et votre mot de passe. Le planning affiche les disponibilités de chaque appareil et les créneaux des instructeurs.</p>
      <p>Merci de respecter les règles de réservation et de libérer vos créneaux si vous ne pouvez pas voler.</p>
      <p class="red-text">Réserver un avion</p>
      <h4>Planavi - Points importants pour la réservation</h4>
      <ul>
        <li>Chaque pilote est responsable de sa réservation et doit la confirmer la veille du vol.</li>
        <li>Une réservation non honorée sans prévenir pourra entraîner une suspension temporaire de l'accès.</li>
        <li>Les élèves doivent réserver en accord avec leur instructeur et préciser le type de leçon.</li>
        <li>Les vols de plus de trois heures nécessitent l'accord préalable du chef pilote.</li>
        <li>En cas de panne, signalez-la au bureau au plus vite.</li>
      </ul>
    </div>
  </div>
</section>

<footer class="site-footer">
  <div class="footer-row">
    <div>
      <p class="footer-title">Siège social, plate-forme aéro-club et adresse postale :</p>
      <div class="footer-cols">
        <div class="address">
          <svg width="14" height="18" viewBox="0 0 14 18"><path d="M7 0C3 0 0 3 0 7c0 5 7 11 7 11s7-6 7-11c0-4-3-7-7-7zm0 10a3 3 0 110-6 3 3 0 010 6z" fill="#fff"/></svg>
          <p>Bâtiment 12<br>Aérodrome de Vauclair<br>78450 Vauclair<br>Téléphone : 01 00 00 00 00</p>
        </div>
        <div class="address">
          <svg width="14" height="18" viewBox="0 0 14 18"><path d="M7 0C3 0 0 3 0 7c0 5 7 11 7 11s7-6 7-11c0-4-3-7-7-7zm0 10a3 3 0 110-6 3 3 0 010 6z" fill="#fff"/></svg>
          <p>Association sans but lucratif loi 1901<br>Agrément jeunesse et sports n° 00-000<br>Affiliée à la Ligue Aérienne de Sorvane<br>Organisme déclaré de formation</p>
        </div>
      </div>
    </div>
    <div class="follow">
      <p class="footer-title">Follow Us</p>
      <div class="social"><span></span><span></span><span></span><span></span><span></span></div>
      <p class="copyright">Aéro-club Velnor · Tous droits réservés</p>
    </div>
  </div>
</footer>
</body>
</html>
```